VerdaloMD is an aesthetics and wellness medical spa. I am looking for a modern site, not too glam, not too boring. Currently I have the coming soon page at verdaloMD.com. The green in the logo is the accent color. I need the site to be semi neutral. I don't want it to be too geared towards females because there are some consults that men also will participate in.

```html
<!DOCTYPE html>
<html lang="en">
<head>
<meta charset="utf-8">
<title>VerdaloMD — Aesthetics &amp; Wellness</title>
<link rel="stylesheet" href="https://fonts.googleapis.com/css2?family=Merriweather:ital,wght@0,400;0,700;1,400&family=Open+Sans:wght@400;500;600&family=Montserrat:wght@500;600&display=swap">
<style>
:root{
  --ink:#1d1d1d;
  --body:#3a3a3a;
  --accent:#f26d5b;
  --mint:#dfede8;
  --mint-mid:#c4e2d8;
  --sage:#9fcfc1;
  --sage-deep:#7fb5a5;
  --footer:#4a4a4a;
  --white:#ffffff;
}
*{margin:0;padding:0;box-sizing:border-box}
html,body{width:1200px;height:4051px;overflow:hidden}
body{position:relative;background:var(--white);font-family:"Open Sans",sans-serif;color:var(--body)}
.abs{position:absolute}
.serif{font-family:"Merriweather",serif}
.btn{position:absolute;display:flex;align-items:center;justify-content:center;background:var(--accent);color:var(--white);border-radius:24px;font-family:"Merriweather",serif;font-size:17px;letter-spacing:.3px;text-transform:uppercase}
.photo{position:absolute}

/* header */
.brand{position:absolute;display:flex;align-items:center;gap:10px;font-family:"Open Sans",sans-serif;font-weight:500;font-size:34px;color:var(--ink);letter-spacing:.2px}
.brand-dot{width:18px;height:18px;border-radius:50%;background:var(--sage-deep)}
.nav{position:absolute;left:600px;top:36px;display:flex;gap:23px;font-family:"Merriweather",serif;font-size:19px;color:var(--ink)}
.nav .active{font-weight:700}

/* hero */
.hero{position:absolute;left:0;top:0;width:1200px;height:708px;overflow:hidden}
.hero-bg{position:absolute;inset:0;background:linear-gradient(100deg,#eef4f0 0%,#f6efe9 45%,#fbf7f4 70%,#ffffff 100%)}
.hero-title{position:absolute;left:100px;top:212px;font-family:"Merriweather",serif;font-weight:700;font-size:47px;line-height:68px;color:var(--ink)}

/* about */
.card-frame{position:absolute;background:var(--white);border-radius:12px;box-shadow:0 10px 22px rgba(0,0,0,.16)}
.section-title{position:absolute;font-family:"Merriweather",serif;font-size:42px;color:var(--ink)}
.copy{position:absolute;font-size:14px;line-height:22.6px;color:var(--body)}

/* services */
.services{position:absolute;left:0;top:1308px;width:1200px;height:748px;background:var(--mint)}
.service{position:absolute;top:185px;width:330px;text-align:center}
.service-photo{width:270px;height:270px;border-radius:50%;margin:0 auto}
.service h3{margin-top:75px;font-family:"Merriweather",serif;font-weight:400;font-size:24px;color:var(--ink)}
.service p{margin-top:12px;font-size:13.5px;line-height:22px;color:var(--body)}

/* testimonials */
.testimonials{position:absolute;left:0;top:2897px;width:1200px;height:566px;background:linear-gradient(180deg,#eef6f3,#e6f1ed)}
.quote{position:absolute;top:183px;width:300px;text-align:center}
.quote-mark{width:98px;height:98px;border-radius:50%;background:var(--mint-mid);margin:0 auto;display:flex;align-items:center;justify-content:center;font-family:"Merriweather",serif;font-weight:700;font-size:92px;line-height:1;color:var(--ink);padding-top:40px}
.quote p{margin-top:36px;font-family:"Merriweather",serif;font-style:italic;font-size:17px;line-height:27px;color:var(--body)}
.quote h4{margin-top:22px;font-family:"Merriweather",serif;font-weight:400;font-size:17px;color:var(--ink)}

/* signup */
.signup{position:absolute;left:0;top:3463px;width:1200px;height:317px;background:linear-gradient(180deg,#abd5c9,#b9dcd1)}
.signup h2{position:absolute;left:0;top:66px;width:1200px;text-align:center;font-family:"Merriweather",serif;font-weight:400;font-size:24px;line-height:30px;color:var(--ink);text-transform:uppercase}
.field{position:absolute;top:172px;width:198px;height:42px;background:var(--white);border-radius:21px;font-size:12px;color:var(--body);padding:14px 0 0 22px}
.signup .btn{top:172px;left:846px;width:198px;height:42px;font-family:"Montserrat",sans-serif;font-weight:600;font-size:16px}

/* footer */
.footer{position:absolute;left:0;top:3780px;width:1200px;height:271px;background:var(--footer);color:var(--white)}
.footer .brand{color:var(--white);left:0;width:1200px;justify-content:center;top:50px;font-size:38px}
.footer-links{position:absolute;top:142px;left:0;width:1200px;display:flex;justify-content:center;gap:40px;font-family:"Montserrat",sans-serif;font-weight:600;font-size:14px}
.footer-legal{position:absolute;top:195px;left:0;width:1200px;display:flex;justify-content:center;gap:34px;font-family:"Montserrat",sans-serif;font-weight:500;font-size:13px}
</style>
</head>
<body>

<!-- HERO -->
<section class="hero">
  <div class="hero-bg" role="img" aria-label="Soft faded photo of a client relaxing at a spa with a lotus flower"></div>
  <svg class="abs" style="left:0;top:0" width="1200" height="708" viewBox="0 0 1200 708">
    <path d="M590 0 H1200 V600 L700 600 C620 480 570 300 575 160 C578 90 585 40 590 0 Z" fill="#e2f1ec"/>
    <circle cx="951" cy="222" r="212" fill="#ffffff"/>
    <path d="M0 600 C250 720 620 640 1200 560 V600 C700 620 300 720 0 660 Z" fill="#a9d3c6"/>
    <path d="M0 660 C300 720 700 620 1200 600 V708 H0 Z" fill="#ffffff"/>
  </svg>
  <div class="photo" style="left:700px;top:134px;width:500px;height:470px;background:radial-gradient(circle at 55% 45%,#f1e3dc 0%,#e6d6cf 40%,#dcd8d6 70%,rgba(255,255,255,0) 72%);border-radius:0 0 0 40px" role="img" aria-label="Woman in a towel wrap wearing a clay face mask, holding cucumber slices"></div>
</section>

<div class="brand" style="left:104px;top:30px"><span class="brand-dot"></span>VerdaloMD</div>
<nav class="nav">
  <span class="active">Home</span><span>About Us</span><span>Services</span><span>Blog</span><span>Contact</span>
</nav>

<h1 class="hero-title">LOOK AND FEEL<br>YOUR BEST</h1>
<div class="btn" style="left:104px;top:374px;width:289px;height:48px">Join our community</div>

<!-- ABOUT -->
<div class="card-frame" style="left:200px;top:794px;width:354px;height:405px"></div>
<div class="photo" style="left:212px;top:806px;width:329px;height:378px;border-radius:6px;background:linear-gradient(160deg,#d9c3b5,#efe4dc 55%,#cfd7da)" role="img" aria-label="Man receiving a facial treatment with a head wrap"></div>
<div class="abs" style="left:512px;top:961px;width:68px;height:68px;border-radius:50%;background:var(--white);border:2px solid var(--mint-mid)"></div>

<h2 class="section-title" style="left:618px;top:786px">About Us</h2>
<p class="copy" style="left:618px;top:853px;width:425px">Sed ut perspiciatis unde omnis iste natus error sit voluptatem accusantium doloremque laudantium, totam rem aperiam, eaque ipsa quae ab illo inventore veritatis et quasi architecto beatae vitae dicta sunt explicabo. Nemo enim ipsam voluptatem quia voluptas sit aspernatur aut odit aut fugit, sed quia consequuntur magni dolores eos qui ratione voluptatem sequi nesciunt. Neque porro quisquam est, qui dolorem ipsum quia dolor sit amet, consectetur, adipisci velit, sed quia non numquam eius modi tempora incidunt ut labore et dolore magnam aliquam quaerat voluptatem.Lorem ipsum dolor sit amet, consectetur adipiscing elit, sed do eiusmod tempor incididunt ut labore et dolore magna aliqua.</p>
<div class="btn" style="left:618px;top:1140px;width:172px;height:44px">Read more</div>

<!-- SERVICES -->
<section class="services">
  <h2 class="section-title" style="left:0;width:1200px;text-align:center;top:88px">Our Services</h2>
  <div class="service" style="left:102px">
    <div class="service-photo" role="img" aria-label="Woman receiving a skin treatment, framed with eucalyptus leaves" style="background:radial-gradient(circle at 60% 40%,#f4e2d8,#cfd9d2 70%,#b9cfc4)"></div>
    <h3>Peptides</h3>
    <p>Lorem ipsum dolor sit amet, consectetur<br>incididunt ut labore et dolore magna aliqua.</p>
  </div>
  <div class="service" style="left:447px">
    <div class="service-photo" role="img" aria-label="Man receiving a dermal filler injection, framed with eucalyptus leaves" style="background:radial-gradient(circle at 60% 40%,#e7d2c4,#c9d4cf 70%,#b3c9be)"></div>
    <h3>Dermal Fillers</h3>
    <p>Lorem ipsum dolor sit amet, consectetur<br>incididunt ut labore et dolore magna aliqua.</p>
  </div>
  <div class="service" style="left:797px">
    <div class="service-photo" role="img" aria-label="Couple receiving relaxing facial massages, framed with eucalyptus leaves" style="background:radial-gradient(circle at 60% 40%,#efd5c4,#d2d6cf 70%,#b8cdc1)"></div>
    <h3>IV Therapy</h3>
    <p>Lorem ipsum dolor sit amet, consectetur<br>incididunt ut labore et dolore magna aliqua.</p>
  </div>
  <div class="btn" style="left:514px;top:639px;width:172px;height:44px">Read more</div>
</section>

<!-- JOURNEY -->
<h2 class="abs serif" style="left:102px;top:2260px;font-size:34px;line-height:45px;font-weight:400;color:var(--ink)">START OR CONTINUE YOUR<br>AESTHETICS AND WELLNESS<br>JOURNEY HERE.</h2>
<p class="copy" style="left:100px;top:2436px;width:430px">Sed ut perspiciatis unde omnis iste natus error sit voluptatem accusantium doloremque laudantium, totam rem aperiam, eaque ipsa quae ab illo inventore veritatis et quasi architecto beatae vitae dicta sunt explicabo. Nemo enim ipsam voluptatem quia voluptas sit aspernatur aut odit aut fugit, sed quia consequuntur magni dolores eos qui ratione voluptatem sincididunt ut labore et dolore magna aliqua.</p>
<div class="card-frame" style="left:628px;top:2191px;width:473px;height:483px;border-radius:26px"></div>
<div class="photo" style="left:640px;top:2203px;width:448px;height:460px;border-radius:0 20px 0 20px;background:linear-gradient(150deg,#d9bfae,#efe1d6 50%,#c9a786)" role="img" aria-label="Woman enjoying a head massage beside candles on a wooden tray"></div>
<div class="photo" style="left:795px;top:2580px;width:310px;height:190px;border-radius:40% 40% 30% 30%;background:radial-gradient(ellipse at 50% 60%,#c9c9c9,#e2dede 60%,rgba(255,255,255,0) 72%)" role="img" aria-label="Stacked spa stones with pink orchids"></div>

<!-- TESTIMONIALS -->
<section class="testimonials">
  <h2 class="section-title" style="left:0;width:1200px;text-align:center;top:85px">Our Happy Clients</h2>
  <svg class="abs" style="left:34px;top:252px" width="32" height="50" viewBox="0 0 32 50"><path d="M28 3 L5 25 L28 47" fill="none" stroke="var(--sage-deep)" stroke-width="3"/></svg>
  <svg class="abs" style="left:1136px;top:252px" width="32" height="50" viewBox="0 0 32 50"><path d="M4 3 L27 25 L4 47" fill="none" stroke="var(--sage-deep)" stroke-width="3"/></svg>
  <div class="quote" style="left:114px"><div class="quote-mark">&ldquo;</div><p>Lorem ipsum dolor sit amet, consectetur adipiscing elit, sed do labore et dolore magna aliqua.</p><h4>JAMES WARD</h4></div>
  <div class="quote" style="left:452px"><div class="quote-mark">&ldquo;</div><p>Lorem ipsum dolor sit amet, consectetur adipiscing elit, sed do labore et dolore magna aliqua.</p><h4>JAMES WARD</h4></div>
  <div class="quote" style="left:790px"><div class="quote-mark">&ldquo;</div><p>Lorem ipsum dolor sit amet, consectetur adipiscing elit, sed do labore et dolore magna aliqua.</p><h4>JAMES WARD</h4></div>
</section>

<!-- SIGNUP -->
<section class="signup">
  <h2>A motivation platform &nbsp;- we are more<br>than a clinic, join our community.</h2>
  <div class="field" style="left:220px">Name:</div>
  <div class="field" style="left:426px">Email:</div>
  <div class="field" style="left:639px">Phone:</div>
  <div class="btn">SIGN UP</div>
</section>

<!-- FOOTER -->
<footer class="footer">
  <div class="brand"><span class="brand-dot" style="background:var(--white)"></span>VerdaloMD</div>
  <div class="footer-links"><span>HOME</span><span>ABOUT</span><span>SERVICES</span><span>TESTIMONIALS</span><span>CONTACT</span></div>
  <div class="footer-legal"><span>© 2022 VerdaloMD</span><span>Terms of Use</span><span>Membership Terms &amp; Conditions</span><span>Privacy Policy</span></div>
</footer>

</body>
</html>
```